I want a double sided flyer possibly with a picture of a lawn or grass.
Company name, phone number, email, and logo
Halvorsen Turf Management, (404)726-1853,Halvorsen_Turf@brevimail.com
Company services
Fertilization and weed control,Lawn and Landscape maintenance, mowing, pruning, aeration, landscape and Christmas lights,

```html
<!DOCTYPE html>
<html lang="en">
<head>
<meta charset="utf-8">
<title>Halvorsen Turf Management Flyer</title>
<link href="https://fonts.googleapis.com/css2?family=Arimo:wght@400;700&display=swap" rel="stylesheet">
<style>
  :root {
    --grass-light: #a9c296;
    --grass-mid: #5f9a45;
    --grass-deep: #3a7f22;
    --grass-dark: #2f6c1b;
    --brand-green: #2f9140;
    --white: #ffffff;
    --ink: #1a1a1a;
    --ink-soft: #3d3d3d;
    --icon-gold: #f2b51c;
  }
  * { margin: 0; padding: 0; box-sizing: border-box; }
  html, body { width: 848px; height: 1200px; overflow: hidden; background: var(--white); }
  body { font-family: "Arimo", Arial, sans-serif; }

  .flyer { position: relative; width: 848px; height: 1200px; overflow: hidden; }

  .lawn-backdrop {
    position: absolute; inset: 0;
    background: linear-gradient(180deg, var(--grass-light) 0%, #8db676 18%, var(--grass-mid) 32%, var(--grass-deep) 55%, var(--grass-dark) 100%);
  }
  .haze-band {
    position: absolute; left: 0; top: 114px; width: 848px; height: 186px;
    background: rgba(255,255,255,0.28);
  }
  .haze-panel {
    position: absolute; left: 150px; top: 71px; width: 548px; height: 359px;
    background: rgba(255,255,255,0.32);
  }

  .brand-card {
    position: absolute; left: 221px; top: 31px; width: 406px; height: 439px;
    background: var(--white);
    display: flex; flex-direction: column; align-items: center;
  }
  .brand-mark {
    width: 130px; height: 130px; margin-top: 60px;
    border-radius: 50%; background: var(--brand-green);
  }
  .brand-name {
    margin-top: 40px; text-align: center;
    color: var(--brand-green); font-weight: 700; line-height: 1.05;
  }
  .brand-name .primary { display: block; font-size: 56px; letter-spacing: 1px; }
  .brand-name .secondary { display: block; font-size: 30px; margin-top: 8px; }

  .content-frame {
    position: absolute; left: 61px; top: 503px; width: 727px; height: 637px;
    border: 5px solid var(--white);
  }

  .panel {
    position: absolute; background: var(--white);
    color: var(--ink); padding: 22px 18px;
  }
  .panel-photo  { left: 88px;  top: 532px; width: 214px; height: 246px; padding: 0;
    background: linear-gradient(160deg, #7fb85e 0%, #4f9a34 55%, #2f7420 100%); }
  .panel-left   { left: 88px;  top: 791px; width: 214px; height: 318px; }
  .panel-middle { left: 315px; top: 664px; width: 215px; height: 445px; }
  .panel-right  { left: 543px; top: 664px; width: 214px; height: 371px; }

  .panel-title {
    font-size: 18px; font-weight: 700; color: var(--brand-green);
    line-height: 1.2; margin-bottom: 12px;
  }
  .panel-copy { font-size: 14px; line-height: 1.45; color: var(--ink-soft); }
  .panel-copy + .panel-copy { margin-top: 10px; }

  .service-list { list-style: none; }
  .service-list li {
    position: relative; padding-left: 20px;
    font-size: 14px; line-height: 1.35; color: var(--ink);
    margin-bottom: 10px;
  }
  .service-list li::before {
    content: ""; position: absolute; left: 2px; top: 3px;
    width: 6px; height: 10px;
    border-right: 2.5px solid var(--brand-green);
    border-bottom: 2.5px solid var(--brand-green);
    transform: rotate(45deg);
  }

  .headline {
    position: absolute; left: 321px; top: 536px;
    color: var(--white); font-weight: 700; font-size: 50px;
    line-height: 0.98; letter-spacing: 1px;
  }

  .contact-card {
    position: absolute; left: 543px; top: 1046px; width: 214px; height: 63px;
    background: var(--white); font-style: normal;
    display: flex; flex-direction: column; justify-content: center; gap: 9px;
    padding-left: 10px;
  }
  .contact-line { display: flex; align-items: center; gap: 7px; font-size: 11.5px; color: var(--ink); white-space: nowrap; }
  .contact-icon { width: 15px; height: 15px; flex: none; }
</style>
</head>
<body>
<main class="flyer">
  <div class="lawn-backdrop" role="img" aria-label="Close-up photograph of a freshly cut green lawn, softly blurred toward the top"></div>
  <div class="haze-band"></div>
  <div class="haze-panel"></div>

  <header class="brand-card">
    <div class="brand-mark"></div>
    <h1 class="brand-name">
      <span class="primary">HALVORSEN</span>
      <span class="secondary">Turf Management</span>
    </h1>
  </header>

  <section class="content-frame"></section>

  <div class="panel panel-photo" role="img" aria-label="Photo of a well-kept, freshly mowed residential lawn"></div>

  <div class="panel panel-left">
    <h3 class="panel-title">Lawn Care Done Right</h3>
    <p class="panel-copy">Healthy, green turf all season long. Our trained crews keep your yard clean, even and thriving.</p>
    <p class="panel-copy">Residential and commercial properties welcome.</p>
  </div>

  <h2 class="headline">PROFESSIONAL<br>SERVICE</h2>

  <div class="panel panel-middle">
    <h3 class="panel-title">Our Services</h3>
    <ul class="service-list">
      <li>Fertilization and weed control</li>
      <li>Lawn maintenance</li>
      <li>Landscape maintenance</li>
      <li>Mowing</li>
      <li>Pruning</li>
      <li>Aeration</li>
      <li>Landscape lighting</li>
      <li>Christmas lights</li>
    </ul>
  </div>

  <div class="panel panel-right">
    <h3 class="panel-title">Seasonal Care</h3>
    <p class="panel-copy">Spring feeding and aeration, summer mowing and pruning, fall cleanup.</p>
    <p class="panel-copy">In winter we design and hang Christmas lights so your home shines for the holidays.</p>
    <p class="panel-copy"><strong>Call today for a free estimate.</strong></p>
  </div>

  <address class="contact-card">
    <div class="contact-line">
      <svg class="contact-icon" viewBox="0 0 16 16" aria-hidden="true">
        <circle cx="8" cy="8" r="8" fill="var(--icon-gold)"/>
        <rect x="5.5" y="3.5" width="5" height="9" rx="1" fill="#3a2a00"/>
        <rect x="6.3" y="4.6" width="3.4" height="5.6" fill="var(--icon-gold)"/>
      </svg>
      <span>(404)726-1853</span>
    </div>
    <div class="contact-line">
      <svg class="contact-icon" viewBox="0 0 16 16" aria-hidden="true">
        <circle cx="8" cy="8" r="8" fill="var(--icon-gold)"/>
        <rect x="4" y="5" width="8" height="6" rx="0.6" fill="#3a2a00"/>
        <path d="M4.4 5.4 L8 8.4 L11.6 5.4" fill="none" stroke="var(--icon-gold)" stroke-width="0.9"/>
      </svg>
      <span>Halvorsen_Turf@brevimail.com</span>
    </div>
  </address>
</main>
</body>
</html>
```